Bday & 7th year in Singapore

I'll be celebrating my thirty something birthday and 7th year in Singapore on Sat 29 June 2013, 830pm til late. Still looking for a venue so please leave some space for it and the address so it can be added.
Required:
Sat, 29 June
830pm
Venue TBC
I would like the poster to have an "infographic" look and feel, ideally with blue, grey, and red tones.
I would like invitees to feel that it's going to a great night of live music, drinks and mingling with existing and new friends so it would be awesome if they can be there.
I love traveling, clubbing, going on food adventures, singing.
People need to know that it's primarily a bday party (main design element) but that I'm also celebrating my 7th year in Singapore.
I'm looking for the most creative design so people will get excited and book their diaries as soon as they see the invitation.
Output required: high quality JPEG I can post on Pindlebox event page and also something I can use for A3 printing. Winning designer should be able to accommodate a revision on venue after decision is made as I can only confirm venue after the deadline.
Reason: Extended the deadline as I realise 2 days is quite tight given nature of the project.
Reason: Waiting for venue to be confirmed so it can be built into the poster
Target Market(s)
Invitees would be between 23 and 35 years old so should appeal to them
Industry/Entity Type
Printing
Requirements
Must have
- Singapore famous landmarks like Corlow Quay Towers, Singapore skyline, Verandine, Tidecrest, but they should not be the centre of attraction
Nice to have
- My photo (attached) but drawn in a nice way

```html
<!DOCTYPE html>
<html lang="en">
<head>
<meta charset="utf-8">
<title>Join My Birthday Party</title>
<link rel="stylesheet" href="https://fonts.googleapis.com/css2?family=Orbitron:wght@600&family=Nunito:wght@800;900&family=Days+One&family=Comfortaa:wght@500&family=Russo+One&family=Quantico:wght@700&display=swap">
<style>
  :root {
    --blue-deep: #3a4ff2;
    --blue-ray: #7d8df6;
    --blue-mid: #3d56f8;
    --blue-teal: #3c86c0;
    --blue-teal-ray: #6aa6d4;
    --red-bright: #ff1d30;
    --red-core: #cc0000;
    --red-fold: #d0101e;
    --maroon: #5c0a14;
    --ink-dark: #1c1c2a;
    --text-cyan: #5fe3f6;
    --text-sky: #8ab4ff;
    --text-violet: #6b6ef2;
    --skyline: #8c2848;
    --performer: #b0101c;
    --crowd: #d81420;
  }
  * { box-sizing: border-box; margin: 0; padding: 0; }
  html, body { width: 849px; height: 1200px; overflow: hidden; background: #fff; }
  .invite { position: relative; width: 849px; height: 1200px; overflow: hidden; background: var(--blue-deep); }
  .layer { position: absolute; left: 0; top: 0; }

  .title-banner {
    position: absolute; left: 35px; top: 5px; width: 800px; height: 120px;
    background: var(--red-bright);
    display: flex; align-items: center; justify-content: center;
  }
  .title-banner h1 {
    font-family: "Orbitron", sans-serif; font-weight: 600; font-size: 46px;
    color: var(--text-cyan); font-variant: small-caps; letter-spacing: 2px; word-spacing: 10px;
    white-space: nowrap; line-height: 1;
  }

  .subtitle-band {
    position: absolute; left: 0; top: 160px; width: 849px; height: 55px;
    background: var(--maroon);
    display: flex; align-items: center; justify-content: center;
  }
  .subtitle-band p {
    font-family: "Nunito", sans-serif; font-weight: 900; font-size: 33px; color: var(--red-bright);
  }

  .bubble {
    position: absolute; background: var(--red-bright); border-radius: 16px;
    box-shadow: 3px 4px 0 rgba(20,10,40,0.55);
  }
  .bubble-inner { position: absolute; background: var(--red-core); border-radius: 16px; }

  .when { left: 12px; top: 222px; width: 415px; height: 234px; }
  .when .bubble-inner { left: 18px; top: 13px; width: 385px; height: 208px; padding: 14px 0 0 18px; color: var(--text-sky); }
  .when .fun { font-family: "Nunito", sans-serif; font-weight: 900; font-size: 40px; letter-spacing: -1px; line-height: 46px; }
  .when .fun small { font-size: 22px; font-weight: 800; letter-spacing: 0; }
  .when .day { font-family: "Days One", sans-serif; font-size: 26px; margin-top: 2px; }
  .when .day small { font-size: 21px; }
  .when .time { font-family: "Days One", sans-serif; font-size: 24px; margin-top: 12px; margin-left: 6px; }
  .when .time small { font-size: 20px; }
  .when .venue { font-family: "Nunito", sans-serif; font-weight: 800; font-size: 18px; margin-top: 14px; margin-left: 6px; line-height: 24px; }

  .music { left: 18px; top: 492px; width: 460px; height: 286px; }
  .music .bubble-inner { left: 17px; top: 18px; width: 427px; height: 250px; padding: 14px 0 0 12px; color: var(--text-sky); }
  .music .lead { font-family: "Comfortaa", sans-serif; font-weight: 500; font-size: 40px; line-height: 58px; }
  .music .hook { font-family: "Days One", sans-serif; font-size: 50px; margin-top: 12px; }

  .beat { left: 422px; top: 893px; width: 410px; height: 282px; }
  .beat .bubble-inner { left: 23px; top: 19px; width: 365px; height: 238px; padding: 10px 0 0 24px; }
  .beat .lead { font-family: "Quantico", sans-serif; font-weight: 700; font-size: 29px; letter-spacing: 2px; word-spacing: 6px; line-height: 58px; color: var(--text-sky); }
  .beat .shout { font-family: "Russo One", sans-serif; font-size: 50px; letter-spacing: 4px; line-height: 54px; color: var(--text-violet); }

  .art { position: absolute; }
  .art-skyline { left: 430px; top: 230px; width: 419px; height: 242px; background: linear-gradient(180deg, #9a3a6a, var(--skyline)); }
  .art-performer { left: 545px; top: 480px; width: 304px; height: 395px; background: linear-gradient(180deg, var(--blue-mid), var(--performer) 30%, #c41c3a); }
  .art-crowd { left: 0; top: 895px; width: 380px; height: 305px; background: linear-gradient(180deg, rgba(216,20,32,0.2), var(--crowd) 35%, #a8101c); }
</style>
</head>
<body>
<main class="invite">
  <svg class="layer" width="849" height="1200" viewBox="0 0 849 1200" aria-hidden="true">
    <rect x="0" y="0" width="849" height="160" fill="var(--blue-deep)"/>
    <polygon points="85,0 165,0 170,160 95,160" fill="var(--blue-ray)"/>
    <polygon points="420,0 510,0 500,160 430,160" fill="var(--blue-ray)"/>
    <polygon points="700,0 780,0 800,160 720,160" fill="var(--blue-ray)"/>
    <rect x="0" y="215" width="849" height="260" fill="var(--blue-deep)"/>
    <polygon points="450,215 560,215 530,472 470,472" fill="var(--blue-ray)"/>
    <polygon points="640,215 780,215 849,300 849,420" fill="var(--blue-ray)"/>
    <polygon points="170,456 230,456 240,472 175,472" fill="var(--blue-ray)"/>
    <rect x="0" y="475" width="849" height="400" fill="var(--blue-mid)"/>
    <rect x="0" y="875" width="849" height="325" fill="var(--blue-teal)"/>
    <polygon points="300,875 360,875 330,1200 250,1200" fill="var(--blue-teal-ray)" opacity="0.6"/>
    <polygon points="200,875 240,875 120,1100" fill="var(--blue-teal-ray)" opacity="0.5"/>
    <polygon points="500,875 560,875 849,1100 849,1180" fill="var(--blue-teal-ray)" opacity="0.4"/>
    <!-- ribbon tails behind the title banner -->
    <polygon points="0,32 60,32 60,146 0,146 22,89" fill="var(--red-fold)"/>
    <polygon points="849,32 789,32 789,146 849,146 827,89" fill="var(--red-fold)"/>
    <polygon points="35,125 35,146 78,146 78,125" fill="var(--ink-dark)"/>
    <polygon points="835,125 835,146 792,146 792,125" fill="var(--ink-dark)"/>
    <polygon points="478,520 540,555 478,552" fill="var(--red-bright)"/>
    <polygon points="424,925 385,948 424,955" fill="var(--red-bright)"/>
  </svg>

  <div class="art art-skyline" role="img" aria-label="Skyline illustration with control tower and Corlow Quay Towers"></div>
  <div class="art art-performer" role="img" aria-label="Silhouette of a guitarist with music notes"></div>
  <div class="art art-crowd" role="img" aria-label="Silhouette of a dancing party crowd"></div>

  <header class="title-banner"><h1>Join My Birthday Party!</h1></header>
  <div class="subtitle-band"><p>Celebrate my 7th years in Singapore</p></div>

  <section class="bubble when">
    <div class="bubble-inner">
      <p class="fun">Fun! <small>starts at,</small></p>
      <p class="day">Saturday, <small>June 29</small></p>
      <p class="time">8:30pm <small>till Late</small></p>
      <p class="venue">Venue: TBC<br>Address to follow</p>
    </div>
  </section>

  <section class="bubble music">
    <div class="bubble-inner">
      <p class="lead">Enjoy the Music<br>that is off the</p>
      <p class="hook">Hook!</p>
    </div>
  </section>

  <section class="bubble beat">
    <div class="bubble-inner">
      <p class="lead">GET DOWN TO THE<br>BEAT WITH THIS</p>
      <p class="shout">FUN<br>PARTY!!</p>
    </div>
  </section>
</main>
</body>
</html>
```